Bifold brochure design for leadership academy

Please see below. This is a bifold brochure for a leadership academy. (www.vesk.institute). Look and feel must be colours, shapes, abstract designs, graphics, pictures. Make this professional, yet casual and bold.

Feel free to design just the front and back cover, then I'll give feedback on whether or not you're in the right direction.

COVER
- Title: “The Brightwater Year Journey”
- “Northmere Pathways Institute” logo somewhere
- Subtitles (with images, icons, and/or shapes): “Self-discovery” “Skills development” “Real-world Impact”

PAGE 2 (Inside Fold)
- Title: "The Program"
- Section 2a: Section title: "How it works”
- Image: See website, image under "four phases of the program". Please adapt and make it look better
- Text: VPI is a structured, 8-month ‘gap year’ program for 18-25 year olds who want more than just a year off – they want a year ahead. Our aim is to develop high-potential young leaders with strong values, clear purpose, high-impact skills, and a track record of real-world accomplishments that are second-to-none. We do this through four-phases.
- Section 2b: Section title: “Dates & Timing”
- Image: See image on website under 'dates and timing'. Make sure both dates show up on the brochure (September and January program).
- Text: There are two programs per year: one that starts in September, the other in January. The first four months of the program are based in Toronto at the VPI headquarters. The curriculum we work through is highly engaging and personalized, focusing directly on students’ goals. After that, students are out in the world, achieving the remaining components of the program (e.g. internship, volunteer abroad).

PAGE 3 (Outside Fold)
- Page Title: "The Students"
- Section 3a: Section title: “Who’s it for”
- Subtitle1: “High school graduates”
 Image/icon of a high school grad
 Text1: 90% of high school grads aren't sure why they’re going to university or what they want to study.
 Text2: VPI helps students discover what they truly want to do in life, and make enormous progress towards these goals.

- Subtitle2: “Post-secondary students”
 Image/icon of a university / college student
 Text1: 28% of students switch or drop out of their program because it wasn’t for them or they didn’t like it.
 Text2: Don't keep moving around or risk switching careers down the road – find out what sparks your passion with VPI.

- Subtitle3: “Post-secondary graduates”
 Image/icon of a university/ college grad
 Text1: 50% of graduates are unemployed or underemployed, 60% are in debt.
 Text2: VPI will help you get your dream job – our students won’t settle for anything less.

- Section 3b: Section title: “How to apply”
 Text1: We select high-potential young leaders with a desire to improve themselves and impact the world.
 Text2: We won’t ask you for your grades – we care more about your values and potential.
 Text3: Visit www.vesk.institute to apply now

BACK COVER
- Page Title: “Get in Touch”
- Website: www.vesk.institute
- Pagebook page: facebook.com/vesk.institute
- Chirplet handle: @vesk_institute
- Email: marta@vesk.institute

Target Market(s)

18-25 year olds, parents, teachers

Industry/Entity Type

Leadership

Requirements
Must have
• Beautiful design - sleek and bold, yet colourful and casual. Keep the colours similar to our website (www.vesk.institute). See examples of other brochures.
• http://img.plorvex.net/jpg/00/11/22/33/240_F_11223344_aBcDeFgHiJkLmNoPqRsTuVwXyZ123456.jpg
• http://quandrelhub.com/wp-content/uploads/2014/11/Real-Estate-Bi-fold-Brochure.jpg
• http://www.trovanic.com/media/k2/galleries/5/001-bi-fold-brochure-psd-mock-up-template.jpg
• http://img.plorvex.net/jpg/00/44/55/66/240_F_44556677_zYxWvUtSrQpOnMlKjIhGfEdCbA987654.jpg

```html
<!DOCTYPE html>
<html lang="en">
<head>
<meta charset="utf-8">
<title>Northmere Pathways Institute – Bifold Brochure</title>
<link rel="stylesheet" href="https://fonts.googleapis.com/css2?family=Roboto:wght@400;500;700;900&family=Roboto+Condensed:wght@700&display=swap">
<style>
  :root {
    --red: #b0191e;
    --red-dark: #8e1216;
    --blue: #7ab6d9;
    --pink: #f3d5d8;
    --ink: #1f1f1f;
    --text: #4a4a4a;
    --panel-grey: #e6e6e6;
    --green: #5a9f2c;
    --beige: #e6d9bb;
    --slate: #5d5f63;
    --stage: #dcdcdc;
    --white: #ffffff;
  }
  * { box-sizing: border-box; margin: 0; padding: 0; }
  html, body { width: 1200px; height: 900px; overflow: hidden; background: var(--stage); }
  body { font-family: "Roboto", Arial, sans-serif; color: var(--ink); }
  .canvas { position: relative; width: 1200px; height: 900px; overflow: hidden; background: var(--stage); }

  .sheet { position: absolute; overflow: hidden; box-shadow: 0 4px 14px rgba(0,0,0,.18); }
  .sheet > svg.shapes { position: absolute; inset: 0; }
  .abs { position: absolute; }

  /* Front cover */
  .front-cover { left: 60px; top: 30px; width: 300px; height: 420px; background: var(--white); }
  .brand-lockup { left: 16px; top: 128px; width: 100px; font-family: "Roboto Condensed", "Arial Narrow", sans-serif; font-weight: 700; color: var(--red); font-size: 17px; line-height: 1.02; text-transform: uppercase; letter-spacing: .5px; }
  .cover-title { left: 0; top: 312px; width: 300px; height: 30px; background: var(--red); color: var(--white); font-weight: 700; font-size: 15px; line-height: 30px; padding-left: 18px; white-space: nowrap; }
  .pillars { left: 10px; top: 362px; width: 284px; display: flex; justify-content: space-between; }
  .pillar { display: flex; align-items: center; gap: 4px; font-size: 9px; font-weight: 700; color: var(--ink); white-space: nowrap; }

  /* Back cover */
  .back-cover { left: 840px; top: 30px; width: 300px; height: 420px; background: var(--pink); }
  .contact-title { left: 0; top: 16px; width: 300px; text-align: center; color: var(--white); font-weight: 700; font-size: 16px; }
  .contact-rule { left: 95px; top: 40px; width: 110px; height: 1px; background: rgba(255,255,255,.8); }
  .contact-line { font-size: 10px; font-weight: 700; display: flex; align-items: flex-start; gap: 5px; line-height: 1.3; white-space: nowrap; }
  .contact-line.on-red { color: var(--white); }
  .contact-line.on-pink { color: var(--text); justify-content: flex-end; text-align: right; }
  .contact-dot { width: 10px; height: 10px; border-radius: 50%; flex: none; margin-top: 2px; }

  /* Inside spread */
  .spread { left: 200px; top: 470px; width: 800px; height: 410px; background: var(--white); }
  .fold { left: 399px; top: 0; width: 2px; height: 410px; background: rgba(0,0,0,.08); }
  .overview-title { left: 14px; top: 10px; color: var(--white); font-weight: 700; font-size: 14px; }
  .overview-text { left: 14px; top: 29px; width: 360px; color: var(--white); font-size: 9px; line-height: 1.3; }
  .students-box { left: 0; top: 72px; width: 112px; height: 42px; background: var(--slate); color: var(--white); padding: 5px 0 0 12px; }
  .students-box h2 { font-size: 13px; font-weight: 700; line-height: 1.1; }
  .students-box p { font-size: 10px; font-weight: 700; }
  .students-intro { left: 122px; top: 76px; width: 240px; color: var(--white); font-size: 6.5px; line-height: 1.3; }

  .audience { left: 28px; width: 280px; }
  .audience-head { display: flex; align-items: flex-end; gap: 6px; }
  .audience-head h3 { font-size: 9px; font-weight: 700; }
  .audience p { font-size: 7px; line-height: 1.35; color: var(--text); margin: 3px 0 0 0; }
  .audience.hs h3 { color: var(--red); }
  .audience.ps h3 { color: var(--green); }
  .audience.apply h3 { color: var(--ink); }
  .apply-cta { left: 0; top: 386px; width: 400px; text-align: center; font-size: 8px; font-weight: 700; color: var(--text); }
  .apply-cta span { color: #2a86c4; }

  .method-text { left: 408px; top: 8px; width: 118px; color: var(--white); font-size: 6.3px; line-height: 1.3; }
  .brand-tag { left: 418px; top: 132px; width: 62px; height: 30px; background: var(--white); color: var(--red); font-weight: 900; font-size: 17px; line-height: 30px; text-align: center; }
  .program-band { left: 418px; top: 174px; color: var(--white); font-weight: 700; font-size: 14px; }
  .phase { width: 60px; text-align: center; }
  .phase-label { font-size: 8px; font-weight: 700; color: var(--ink); margin-top: 3px; }
  .col-head { font-size: 11px; font-weight: 700; color: var(--red); }
  .col-text { font-size: 6.4px; line-height: 1.3; color: var(--text); margin-top: 4px; }
</style>
</head>
<body>
<main class="canvas">

  <!-- FRONT COVER -->
  <section class="sheet front-cover" aria-label="Front cover">
    <svg class="shapes" width="300" height="420" viewBox="0 0 300 420" aria-hidden="true">
      <polygon points="0,0 175,0 0,118" fill="var(--red)"/>
      <polygon points="300,40 300,270 186,155" fill="var(--red)"/>
      <polygon points="140,296 300,296 300,312 128,312" fill="var(--red-dark)"/>
    </svg>
    <svg class="abs" style="left:0;top:0" width="300" height="420" viewBox="0 0 300 420" role="img" aria-label="Photo of a businessman facing a wall of chalk-drawn ideas">
      <defs>
        <linearGradient id="frontPhoto" x1="0" y1="0" x2="0" y2="1">
          <stop offset="0" stop-color="#8a8d91"/>
          <stop offset="1" stop-color="#3d3f43"/>
        </linearGradient>
      </defs>
      <polygon points="125,62 252,62 252,222 208,296 125,296" fill="url(#frontPhoto)"/>
    </svg>
    <svg class="abs" style="left:0;top:0" width="300" height="420" viewBox="0 0 300 420" aria-hidden="true">
      <rect x="140" y="8" width="72" height="54" fill="var(--blue)"/>
    </svg>
    <div class="abs brand-lockup">Northmere<br>Pathways<br>Institute</div>
    <div class="abs cover-title">The Brightwater Year Journey</div>
    <div class="abs pillars">
      <div class="pillar">
        <svg width="14" height="14" viewBox="0 0 14 14" aria-hidden="true"><circle cx="7" cy="7" r="7" fill="var(--slate)"/><ellipse cx="7" cy="7" rx="4.5" ry="2.6" fill="none" stroke="#fff" stroke-width="1.2"/><circle cx="7" cy="7" r="1.2" fill="#fff"/></svg>
        Real-world Impact
      </div>
      <div class="pillar">
        <svg width="14" height="14" viewBox="0 0 14 14" aria-hidden="true"><circle cx="7" cy="7" r="5" fill="none" stroke="#2e8fd0" stroke-width="3" stroke-dasharray="2.2 1.4"/><circle cx="7" cy="7" r="2.6" fill="#2e8fd0"/></svg>
        Skills development
      </div>
      <div class="pillar">
        <svg width="14" height="14" viewBox="0 0 14 14" aria-hidden="true"><circle cx="7" cy="6" r="5.5" fill="var(--ink)"/><rect x="4" y="10" width="5" height="4" fill="var(--ink)"/><circle cx="7" cy="5.5" r="1.8" fill="#fff"/></svg>
        Self-discovery
      </div>
    </div>
  </section>

  <!-- BACK COVER -->
  <section class="sheet back-cover" aria-label="Back cover">
    <svg class="shapes" width="300" height="420" viewBox="0 0 300 420" aria-hidden="true">
      <polygon points="0,0 300,0 0,300" fill="var(--red)"/>
    </svg>
    <svg class="abs" style="left:0;top:0" width="300" height="420" viewBox="0 0 300 420" role="img" aria-label="Photo of a smiling graduate raising a diploma against a pale sky">
      <defs>
        <linearGradient id="backPhoto" x1="0" y1="0" x2="0" y2="1">
          <stop offset="0" stop-color="#b9c3cf"/>
          <stop offset="1" stop-color="#6f7883"/>
        </linearGradient>
      </defs>
      <polygon points="150,196 262,300 226,372 74,372 38,300" fill="url(#backPhoto)"/>
    </svg>
    <svg class="abs" style="left:0;top:0" width="300" height="420" viewBox="0 0 300 420" aria-hidden="true">
      <polygon points="196,420 300,330 300,420" fill="var(--slate)"/>
      <polygon points="226,372 300,330 300,372" fill="#7a7c80"/>
    </svg>
    <h1 class="abs contact-title">Get in Touch</h1>
    <div class="abs contact-rule"></div>
    <div class="abs contact-line on-red" style="left:18px;top:60px;">
      <span class="contact-dot" style="background:#fff"></span>Website: www.vesk.institute
    </div>
    <div class="abs contact-line on-red" style="left:18px;top:84px;">
      <span class="contact-dot" style="background:#fff"></span>Pagebook page: pagebook.com/<br>vesk.institute
    </div>
    <div class="abs contact-line on-pink" style="right:14px;top:160px;">
      Chirplet handle: @vesk_institute<span class="contact-dot" style="background:#2e8fd0"></span>
    </div>
    <div class="abs contact-line on-pink" style="right:14px;top:180px;">
      Email: marta@vesk.institute<span class="contact-dot" style="background:var(--ink)"></span>
    </div>
  </section>

  <!-- INSIDE SPREAD -->
  <section class="sheet spread" aria-label="Inside spread">
    <svg class="shapes" width="800" height="410" viewBox="0 0 800 410" aria-hidden="true">
      <rect x="400" y="0" width="400" height="410" fill="var(--panel-grey)"/>
      <polygon points="0,0 400,0 400,260 0,95" fill="var(--blue)"/>
      <polygon points="400,0 560,0 400,250" fill="var(--blue)"/>
      <rect x="560" y="0" width="70" height="40" fill="var(--beige)"/>
      <rect x="700" y="0" width="60" height="40" fill="#2b7fc0"/>
      <polygon points="400,168 624,168 600,206 400,206" fill="var(--ink)"/>
      <polygon points="400,206 600,206 596,212 400,212" fill="var(--red)"/>
      <polygon points="760,110 800,70 800,82 772,110" fill="var(--red)"/>
    </svg>
    <svg class="abs" style="left:0;top:0" width="800" height="410" viewBox="0 0 800 410" role="img" aria-label="Photos of students learning together in a classroom">
      <defs>
        <linearGradient id="classPhoto" x1="0" y1="0" x2="1" y2="1">
          <stop offset="0" stop-color="#d9a7a3"/>
          <stop offset="1" stop-color="#6b4b55"/>
        </linearGradient>
      </defs>
      <polygon points="510,40 700,40 700,160 600,160" fill="url(#classPhoto)"/>
      <polygon points="705,44 800,44 800,70 760,110 705,110" fill="#5c6f8a"/>
    </svg>
    <div class="abs fold"></div>

    <h2 class="abs overview-title">PROGRAM OVERVIEW</h2>
    <p class="abs overview-text">The Northmere Pathways Institute™ (VPI) is a structured, 8-month ‘gap year’ program for 18-25 year olds who want a year of transformation and achievement.</p>
    <div class="abs students-box"><h2>The Students</h2><p>Who’s it for</p></div>
    <p class="abs students-intro">Too many young people drift without direction or purpose, practical skills, or real-world experience. We change that by developing high-potential young leaders with strong values, clear purpose, high-impact skills, and a record of real accomplishments.</p>

    <div class="abs audience hs" style="top:130px;">
      <div class="audience-head">
        <svg width="18" height="14" viewBox="0 0 18 14" aria-hidden="true"><polygon points="9,0 18,4 9,8 0,4" fill="var(--red)"/><path d="M4 6 v4 q5 3 10 0 v-4 l-5 2 z" fill="var(--red)"/></svg>
        <h3>High school graduates</h3>
      </div>
      <p>90% of high school grads aren’t sure why they’re going to university or what they want to study.</p>
      <p>VPI helps students discover what they truly want to do in life, and make enormous progress towards these goals.</p>
    </div>

    <div class="abs audience ps" style="top:212px;">
      <div class="audience-head">
        <svg width="16" height="16" viewBox="0 0 16 16" aria-hidden="true"><polygon points="8,0 16,3 8,6 0,3" fill="var(--green)"/><circle cx="8" cy="8.5" r="3" fill="var(--green)"/><path d="M2 16 q6 -7 12 0 z" fill="var(--green)"/></svg>
        <h3>Post-secondary students</h3>
      </div>
      <p>28% of students switch or drop out of their program because it wasn’t for them or they didn’t like it.</p>
      <p>Don’t keep moving around or risk switching careers down the road – find out what sparks your passion with VPI.</p>
    </div>

    <div class="abs audience apply" style="top:292px;width:340px;">
      <div class="audience-head">
        <svg width="16" height="16" viewBox="0 0 16 16" aria-hidden="true"><rect x="1" y="3" width="11" height="12" fill="none" stroke="var(--ink)" stroke-width="1.6"/><polygon points="13,0 16,3 8,11 5,11 5,8" fill="var(--ink)"/></svg>
        <h3>How to apply</h3>
      </div>
      <p>We select high-potential young leaders with a desire to improve themselves and impact the world.</p>
      <p>We won’t ask you for your grades – we care more about your values and potential.</p>
    </div>

    <p class="abs apply-cta">Visit <span>www.vesk.institute</span> to apply now</p>

    <p class="abs method-text">VPI’s program is founded on a proven leadership development approach, which takes students through a four-phase journey of self-discovery, skills and impact.</p>
    <div class="abs brand-tag">VPI</div>
    <h2 class="abs program-band">The Program</h2>

    <div class="abs phase" style="left:420px;top:214px;">
      <svg width="32" height="32" viewBox="0 0 32 32" aria-hidden="true"><circle cx="16" cy="16" r="16" fill="var(--red)"/><ellipse cx="16" cy="16" rx="9" ry="5" fill="none" stroke="#fff" stroke-width="2"/><circle cx="16" cy="16" r="2.5" fill="#fff"/></svg>
      <div class="phase-label">Discover</div>
    </div>
    <div class="abs phase" style="left:492px;top:214px;">
      <svg width="32" height="32" viewBox="0 0 32 32" aria-hidden="true"><circle cx="16" cy="16" r="16" fill="var(--red)"/><circle cx="16" cy="16" r="8" fill="#fff"/><circle cx="13" cy="13" r="1.6" fill="var(--red)"/><circle cx="19" cy="13" r="1.6" fill="var(--red)"/><circle cx="13" cy="19" r="1.6" fill="var(--red)"/></svg>
      <div class="phase-label">Design</div>
    </div>
    <div class="abs phase" style="left:648px;top:176px;">
      <svg width="32" height="32" viewBox="0 0 32 32" aria-hidden="true"><circle cx="16" cy="16" r="16" fill="var(--red)"/><circle cx="14" cy="9" r="3" fill="#fff"/><path d="M10 24 l3 -10 h3 l2 6 h4 v3 h-6 l-1 -3 -2 4 z" fill="#fff"/></svg>
      <div class="phase-label">Build</div>
    </div>
    <div class="abs phase" style="left:722px;top:164px;">
      <svg width="32" height="32" viewBox="0 0 32 32" aria-hidden="true"><circle cx="16" cy="16" r="16" fill="var(--red)"/><path d="M10 8 h12 v4 q0 6 -6 7 q-6 -1 -6 -7 z" fill="#fff"/><rect x="14.5" y="19" width="3" height="4" fill="#fff"/><rect x="11" y="23" width="10" height="2.5" fill="#fff"/></svg>
      <div class="phase-label">Achieve</div>
    </div>

    <div class="abs" style="left:414px;top:280px;width:178px;">
      <h3 class="col-head">How it works</h3>
      <p class="col-text">VPI is a structured, 8-month ‘gap year’ program for 18-25 year olds who want more than just a year off – they want a year ahead. Our aim is to develop high-potential young leaders with strong values, clear purpose, high-impact skills, and a track record of real-world accomplishments that are second-to-none. We do this through four-phases.</p>
    </div>
    <div class="abs" style="left:606px;top:262px;width:182px;">
      <h3 class="col-head">Dates &amp; Timing</h3>
      <p class="col-text">There are two programs per year: one that starts in September, the other in January. The first four months of the program are based in Toronto at the VPI headquarters. The curriculum we work through is highly engaging and personalized, focusing directly on students’ goals. After that, students are out in the world, achieving the remaining components of the program (e.g. internship, volunteer abroad).</p>
    </div>
  </section>

</main>
</body>
</html>
```